Design a Consultation and HR Services Website "Bright Paths"

Consultation and HR Services
I am looking for a design gives the look and feel of Varden Holt and Quillmere
we need a high-quality graphics website that looks rich and expensive.
we are working as an affiliate for international consultation firms and sole agent for international HR products.
we are a group of consultants for the Middle East.
we will get the global practices to local practices.
Updates

Project Deadline Extended
Reason: I am not getting enough options and designs. I am not getting what I was looking for in matter of look and feel. looking for something rich and luxury with black background and rich font. www.gridmarlow.com www.benitavoss.com 17kendalrow.com/ www.trulo.cc/rd/en/ pemberfold.com/ www.trulo.cc/rd/en/ www.zolmi.com/ www.thegildings.co.uk/ .

Target Market(s)

Corporate all size and industries in GCC

Industry/Entity Type

Management Consulting

Coding

Coded - Design and coding required

Number of Pages Required

5+ page

Font styles to use
Sans Serif
Script

Colors
ffffff
ecf7fb
cee9f5
85cae6
33a6d7
0592cd
000000
848484

Requirements
Must have
• This is the looks and feel that I'm looking for.
• http://www.gridmarlow.com/?channel=display&subchannel=pagemuse
• http://www.benitavoss.com/bvny-private/en/
• http://17kendalrow.com/
• http://www.trulo.cc/rd/en/
• http://pemberfold.com/
• http://www.zolmi.com/
• http://www.thegildings.co.uk/
• Home
• Who we are?
• What we do?
• HR & OD Consultation
• Executive Coaching
• Assesment Cemter
• HRIS & Outsourcing
• Testimonials
• Our Partners
• Contact Us
• We need support on Technical righting...

```html
<!DOCTYPE html>
<html lang="en">
<head>
<meta charset="utf-8">
<title>Bright Paths — International Consultation &amp; HR Services</title>
<link rel="stylesheet" href="https://fonts.googleapis.com/css2?family=Lato:wght@300;400;700&display=swap">
<style>
  :root {
    --white: #ffffff;
    --brand-blue: #33a6d7;
    --brand-deep: #0592cd;
    --ink: #000000;
    --grey: #848484;
    --band: #f4f4f4;
    --divider: #dcdcdc;
    --hero-dark: #2b2d31;
    --hero-mid: #4a4c50;
  }
  * { box-sizing: border-box; margin: 0; padding: 0; }
  html, body { width: 1200px; height: 731px; overflow: hidden; background: var(--white); }
  body { font-family: "Lato", sans-serif; position: relative; }
  a { text-decoration: none; color: inherit; }

  .hero { position: absolute; left: 0; top: 0; width: 1200px; height: 539px; overflow: hidden; }
  .hero-photo {
    position: absolute; inset: 0;
    background:
      radial-gradient(ellipse at 30% 20%, rgba(120,122,126,.55), transparent 55%),
      radial-gradient(ellipse at 80% 35%, rgba(140,140,142,.45), transparent 50%),
      linear-gradient(180deg, var(--hero-mid) 0%, var(--hero-dark) 100%);
  }

  .brand { position: absolute; left: 86px; top: 74px; display: flex; align-items: center; gap: 8px; }
  .brand-mark { width: 12px; height: 12px; background: var(--brand-blue); }
  .brand-name { font-weight: 700; font-size: 20px; color: var(--brand-blue); letter-spacing: .3px; }

  .main-nav { position: absolute; top: 61px; right: 115px; display: flex; gap: 22px; }
  .main-nav a { color: var(--white); font-size: 14px; font-weight: 400; position: relative; }
  .main-nav .has-sub::after {
    content: ""; position: absolute; left: 50%; top: 20px; width: 4px; height: 4px;
    border-right: 1px solid var(--white); border-bottom: 1px solid var(--white);
    transform: translateX(-50%) rotate(45deg);
  }

  .slide-arrow { position: absolute; top: 284px; width: 32px; height: 94px; }
  .slide-arrow.prev { left: 45px; }
  .slide-arrow.next { left: 1114px; }

  .hero-copy { position: absolute; left: 126px; top: 284px; width: 556px; color: var(--white); }
  .hero-title { font-weight: 700; font-size: 51px; line-height: 44px; letter-spacing: -1.8px; white-space: nowrap; }
  .hero-rule { height: 2px; background: var(--brand-blue); margin-top: 18px; }
  .hero-text { font-size: 11.5px; line-height: 16px; margin-top: 20px; width: 545px; }

  .contact-band { position: absolute; left: 0; top: 539px; width: 1200px; height: 78px; background: var(--band); }
  .contact-item { position: absolute; top: 0; height: 78px; display: flex; align-items: center; gap: 16px; color: var(--grey); font-size: 14px; font-weight: 400; }
  .contact-item svg { width: 18px; height: 18px; }
  .contact-item.phone { left: 85px; }
  .contact-item.email { left: 275px; }
  .contact-item.web { left: 524px; }
  .divider { position: absolute; top: 10px; width: 1px; height: 57px; background: var(--divider); }
  .social { position: absolute; left: 993px; top: 32px; display: flex; gap: 18px; }
  .social span { width: 14px; height: 14px; border-radius: 50%; background: var(--grey); display: block; }
  .social span:first-child { background: var(--brand-deep); }

  .site-footer { position: absolute; left: 0; top: 617px; width: 1200px; height: 114px; }
  .copyright { position: absolute; left: 86px; top: 51px; font-size: 10px; color: var(--ink); letter-spacing: -.3px; }
  .footer-brand { position: absolute; left: 972px; top: 47px; display: flex; align-items: center; gap: 8px; }
  .footer-brand .brand-mark { background: var(--ink); }
  .footer-brand .brand-name { color: var(--ink); font-size: 17px; }
</style>
</head>
<body>
  <section class="hero">
    <div class="hero-photo" role="img" aria-label="Photo of business consultants reviewing charts together in a meeting"></div>

    <a class="brand" href="#"><span class="brand-mark"></span><span class="brand-name">Bright Paths</span></a>

    <nav class="main-nav">
      <a href="#">HOME</a>
      <a href="#">WHO WE ARE?</a>
      <a href="#" class="has-sub">SERVICES</a>
      <a href="#">TESTIMONIALS</a>
      <a href="#">OUR PARTNERS</a>
      <a href="#">CONTACT US</a>
    </nav>

    <svg class="slide-arrow prev" viewBox="0 0 32 94" aria-label="Previous slide"><polyline points="30,2 2,47 30,92" fill="none" stroke="#fff" stroke-width="3"/></svg>
    <svg class="slide-arrow next" viewBox="0 0 32 94" aria-label="Next slide"><polyline points="2,2 30,47 2,92" fill="none" stroke="#fff" stroke-width="3"/></svg>

    <div class="hero-copy">
      <h1 class="hero-title">Best<br>International Consultation<br>&amp; HR Services</h1>
      <div class="hero-rule"></div>
      <p class="hero-text">Lorem Ipsum is simply dummy text of the printing and typesetting industry. Lorem Ipsum has been the industry's standard dummy text ever since the 1500s, when an unknown printer took a galley of type and scrambled it to make a type specimen book.</p>
    </div>
  </section>

  <section class="contact-band">
    <div class="contact-item phone">
      <svg viewBox="0 0 18 18"><path d="M4 2 L7 5 L5.5 7 Q7 10.5 11 12.5 L13 11 L16 14 L14 16 Q7 15 2 4 Z" fill="none" stroke="#848484" stroke-width="1.2"/></svg>
      <span>000-000-0000</span>
    </div>
    <div class="divider" style="left:245px"></div>
    <div class="contact-item email">
      <svg viewBox="0 0 18 18"><rect x="1.5" y="4" width="15" height="10" fill="none" stroke="#848484" stroke-width="1.2"/><polyline points="1.5,4 9,10 16.5,4" fill="none" stroke="#848484" stroke-width="1.2"/></svg>
      <span>info@brightpaths.com</span>
    </div>
    <div class="divider" style="left:490px"></div>
    <div class="contact-item web">
      <svg viewBox="0 0 18 18"><circle cx="9" cy="9" r="7.5" fill="none" stroke="#848484" stroke-width="1.2"/><ellipse cx="9" cy="9" rx="3.5" ry="7.5" fill="none" stroke="#848484" stroke-width="1.2"/><line x1="1.5" y1="9" x2="16.5" y2="9" stroke="#848484" stroke-width="1.2"/></svg>
      <span>www.brightpaths.com</span>
    </div>
    <div class="social" aria-label="Social links"><span></span><span></span><span></span><span></span></div>
  </section>

  <footer class="site-footer">
    <p class="copyright">© 2015 BRIGHT PATHS. All rights reserved.</p>
    <div class="footer-brand"><span class="brand-mark"></span><span class="brand-name">Bright Paths</span></div>
  </footer>
</body>
</html>
```